Web site design for Brivolt Software (www.brivoltsoftware-example.com)

Need the design as well as the html for the website. The brief is given in the attached file.
If possible, would like to use pencil sketches instead of images to give a unique look to the site.
Target Market(s)
small Software product companies
Industry/Entity Type
Software
Coding
Coded - Design and coding required
Number of Pages Required
5+ page

```html
<!DOCTYPE html>
<html lang="en">
<head>
<meta charset="utf-8">
<title>Brivolt Software</title>
<link rel="stylesheet" href="https://fonts.googleapis.com/css2?family=Montserrat:wght@400;500;600;700&family=Open+Sans:wght@400;600&display=swap">
<style>
:root{
  --yellow:#f7b500;
  --ink:#1e1e1e;
  --dark:#1b1b1b;
  --bar:#222222;
  --text:#555555;
  --light:#efeeea;
  --grey-band:#8c8c8c;
  --white:#ffffff;
  --line:#e6e6e6;
}
*{margin:0;padding:0;box-sizing:border-box}
html,body{width:1200px;height:3557px;overflow:hidden}
body{font-family:"Open Sans",Arial,sans-serif;color:var(--text);background:var(--white);position:relative}
.heading{font-family:"Montserrat",Arial,sans-serif;color:var(--ink);font-weight:700}
.underline{display:block;width:46px;height:4px;background:var(--yellow);margin:14px auto 0}
section,header,footer{position:absolute;left:0;width:1200px}

/* top bar */
.topbar{top:0;height:34px;background:var(--bar);color:#ddd;font-size:11px;font-family:"Montserrat",sans-serif;display:flex;align-items:center;padding:0 90px}
.topbar .info{display:flex;gap:22px;align-items:center}
.topbar .info span{display:flex;align-items:center;gap:6px}
.topbar .links{margin-left:auto;display:flex;gap:24px;font-weight:500}

/* nav */
.nav{top:34px;height:90px;background:var(--white);display:flex;align-items:center;padding:0 50px 0 90px;border-bottom:1px solid var(--line)}
.logo{display:flex;align-items:center;gap:12px;font-family:"Montserrat",sans-serif;font-weight:700;font-size:27px;color:var(--ink)}
.logo i{width:36px;height:36px;background:var(--yellow);border-radius:6px;display:block}
.menu{margin-left:auto;display:flex;gap:42px;font-family:"Montserrat",sans-serif;font-size:14px;color:#666;height:100%}
.menu a{display:flex;align-items:center;position:relative;color:inherit;text-decoration:none}
.menu a.active{color:var(--ink)}
.menu a.active::after{content:"";position:absolute;left:0;right:0;bottom:0;height:3px;background:var(--yellow)}
.side-tab{position:absolute;left:10px;top:100px;width:26px;height:26px;background:var(--ink);display:flex;align-items:center;justify-content:center}
.side-tab b{width:8px;height:8px;border-radius:50%;background:var(--yellow)}

/* hero */
.hero{top:124px;height:443px;background:var(--yellow);overflow:hidden}
.hero-photo{position:absolute;right:0;top:0;width:700px;height:443px;background:linear-gradient(100deg,var(--yellow) 0%,#c9a02a 22%,#6e6040 55%,#3b352b 100%)}
.hero-quote{position:absolute;left:90px;top:40px;font-family:"Montserrat",sans-serif;font-weight:700;font-size:72px;line-height:80px;color:var(--white)}
.hero-author{position:absolute;left:90px;top:340px;font-size:18px;color:var(--white)}

/* projects */
.projects{top:567px;height:527px;text-align:center}
.eyebrow{font-family:"Montserrat",sans-serif;font-size:11px;letter-spacing:1px;text-transform:uppercase;color:#555}
.projects .eyebrow{margin-top:58px}
.projects h2{font-size:34px;margin-top:8px}
.copy{width:890px;margin:22px auto 0;text-align:left;font-size:13px;line-height:25px}
.copy p+p{margin-top:13px}

/* offer */
.offer{top:1094px;height:630px;background:var(--dark);overflow:hidden;text-align:center}
.offer-texture{position:absolute;inset:0;background:linear-gradient(160deg,#2a2a2a 0%,#151515 55%,#202020 100%)}
.offer h2{position:relative;color:var(--white);font-size:30px;margin-top:72px}
.offer-grid{position:relative;display:grid;grid-template-columns:repeat(5,180px);justify-content:center;row-gap:48px;margin-top:62px}
.offer-item{display:flex;flex-direction:column;align-items:center;padding:0 12px}
.offer-item svg{width:40px;height:40px;stroke:var(--yellow);fill:none;stroke-width:2}
.offer-item h3{font-family:"Montserrat",sans-serif;font-size:11.5px;font-weight:700;color:var(--white);margin-top:10px;white-space:nowrap}
.offer-item h3::after{content:"";display:block;width:24px;height:2px;background:var(--yellow);margin:6px auto 0}
.offer-item p{font-size:10px;line-height:17px;color:#cfcfcf;margin-top:7px}

/* testimonials */
.testimonials{top:1724px;height:526px;background:var(--light);text-align:center}
.testimonials .eyebrow{margin-top:62px;font-size:10px}
.testimonials h2{font-size:26px;line-height:31px;margin-top:6px}
.quote-grid{width:694px;margin:20px auto 0;display:grid;grid-template-columns:repeat(4,173.5px);grid-template-rows:repeat(2,152px)}
.portrait{background:linear-gradient(135deg,#d9d9d9,#8e8e8e 60%,#5d5d5d)}
.quote{background:var(--white);display:flex;flex-direction:column;justify-content:center;padding:0 18px;text-align:left;font-size:10px;line-height:15px;color:#666}
.quote cite{font-style:normal;font-weight:600;color:var(--ink);margin-top:8px;font-size:10.5px}

/* background */
.background{top:2250px;height:539px;text-align:center}
.background h2{font-size:30px;margin-top:50px}
.background .copy{margin-top:24px;line-height:25px}
.background .copy p+p{margin-top:15px}

/* clients */
.clients{top:2789px;height:378px;background:var(--grey-band);text-align:center}
.clients h2{font-size:32px;margin-top:80px}
.client-row{display:flex;justify-content:center;gap:27px;margin-top:45px}
.client{width:147px;height:147px;background:#f4f4f4;display:flex;align-items:center;justify-content:center;gap:8px;font-family:"Montserrat",sans-serif;font-weight:600;font-size:14px;color:#333}
.client i{width:10px;height:10px;border-radius:50%;background:#333;display:block}

/* footer */
.footer{top:3167px;height:390px;background:#151515;color:#d6d6d6;font-size:11px;line-height:18px}
.footer-texture{position:absolute;inset:0;background:linear-gradient(180deg,#1a1a1a,#101010)}
.footer-col{position:absolute;top:96px}
.footer-col .label{font-family:"Montserrat",sans-serif;font-size:9.5px;text-transform:uppercase;color:#bbb;letter-spacing:.5px}
.footer-col h4{font-family:"Montserrat",sans-serif;font-size:14px;color:var(--white);font-weight:700;margin-top:4px}
.footer-col h4::after{content:"";display:block;width:30px;height:3px;background:var(--yellow);margin-top:6px}
.footer-col p{margin-top:10px;width:210px}
.contact-list{list-style:none;margin-top:12px}
.contact-list li{display:flex;gap:8px;align-items:center;margin-bottom:8px}
.contact-list svg{width:12px;height:12px;fill:var(--white)}
.world-map{position:absolute;left:379px;top:170px;width:212px;height:120px;background:radial-gradient(ellipse at 50% 50%,#6e6e6e,#3a3a3a 70%,transparent 72%)}
.network{position:absolute;left:612px;top:170px}
.network .label{font-family:"Montserrat",sans-serif;font-size:9.5px;color:#bbb}
.network li{list-style:none;display:flex;gap:6px;align-items:center;margin-top:8px;font-size:10px}
.network svg{width:10px;height:12px;fill:var(--yellow)}
.social{display:flex;gap:8px;margin-top:14px}
.social span{width:30px;height:30px;border-radius:50%;background:var(--yellow);display:block}
</style>
</head>
<body>

<header class="topbar">
  <div class="info">
    <span><svg width="11" height="11" viewBox="0 0 12 12"><circle cx="6" cy="6" r="5" fill="none" stroke="#fff" stroke-width="1.4"/><path d="M6 3v3l2 1.5" stroke="#fff" stroke-width="1.4" fill="none"/></svg>Working hours&nbsp; Mon - Sat 8.00 - 18.00</span>
    <span><svg width="11" height="11" viewBox="0 0 12 12"><path d="M2 1l3 1 0 3-1.5 1a7 7 0 0 0 3 3l1-1.5 3 0 1 3c-6 1-11-4-9.5-9.5z" fill="#fff"/></svg>Call Us&nbsp; (+1) 555 010-4477</span>
  </div>
  <nav class="links"><span>Case Studies</span><span>Work With us</span><span>Partners</span><span>Stories</span><span>Blog</span><span>Contact</span></nav>
</header>

<header class="nav">
  <div class="logo"><i></i>brivolt</div>
  <nav class="menu">
    <a class="active">Home</a><a>About us</a><a>Services</a><a>Expertise</a><a>Engagement Models</a><a>Agile</a><a>Accolades</a>
  </nav>
</header>
<div class="side-tab"><b></b></div>

<section class="hero">
  <div class="hero-photo" role="img" aria-label="Sketch-style portrait of an engineer in a hard hat, toned yellow and grey"></div>
  <div class="hero-quote">“Create,<br>Enhance<br>and Sustain.“</div>
  <div class="hero-author">Tom Hardell / Chief Executive Officer</div>
</section>

<section class="projects">
  <div class="eyebrow">Learn more about</div>
  <h2 class="heading">Our Projects</h2>
  <span class="underline"></span>
  <div class="copy">
    <p>Design pervades nature. Whether it is the unique symmetry of a snowflake, or the fibonnacci number of a sunflower or nautilus shell, or self replicating fractals, design is everywhere.</p>
    <p>In todays world, Good Design is associated more with tangible products, and User interfaces. But good design has always been part of software engineering. Good design is what enables massive software edifices to remain stable. Good design is UI and UX of course, but it also the process of deciding "what" is required, "how" it is to be built, "who" will build it, and how will its goodness perpetuate itself.</p>
    <p>We are a small but eclectic group of seasoned programmers who infuse rigor and design into solid engineering in software.</p>
    <p>We love to explore new frontiers in technology – be it Predictive Analytics, Cognitive IOT or AI We infuse design into rigorous engineering – not only in software design and UI, but also by using design thinking for deciding what to build; using design for designing the organisational structure of hierarchies, collaborations and communities; for designing the most productive work spaces and processes; and also communities which perpetuate and replicate themselves.</p>
  </div>
</section>

<section class="offer">
  <div class="offer-texture" role="img" aria-label="Dark toned photo of engineers at work, used as section backdrop"></div>
  <h2 class="heading">What We Offer</h2>
  <span class="underline" style="position:relative"></span>
  <div class="offer-grid">
    <div class="offer-item"><svg viewBox="0 0 40 40"><path d="M20 4c6 8 10 13 10 20a10 10 0 0 1-20 0c0-7 4-12 10-20z"/></svg><h3>POC</h3><p>Whether it is a mobile or web app prototype, or a more complex build.</p></div>
    <div class="offer-item"><svg viewBox="0 0 40 40"><circle cx="20" cy="20" r="15"/><path d="M20 20l8-6M12 26h16"/></svg><h3>Build product</h3><p>Our team of analysts, design thinkers and technologists work with client and</p></div>
    <div class="offer-item"><svg viewBox="0 0 40 40"><path d="M10 30l14-14 6 6-14 14H10z"/><path d="M24 16l4-8 6 6-8 4"/></svg><h3>Maintain product</h3><p>We have the ability to quickly understand large, legacy products, write</p></div>
    <div class="offer-item"><svg viewBox="0 0 40 40"><path d="M8 32L32 8M8 8l24 24M6 6h6v6M28 28h6v6"/></svg><h3>ODC setup</h3><p>We help in setting up Offshore Development centres for small and medium</p></div>
    <div class="offer-item"><svg viewBox="0 0 40 40"><path d="M20 4c6 8 10 13 10 20a10 10 0 0 1-20 0c0-7 4-12 10-20z"/><path d="M20 18v10"/></svg><h3>Architectural interventions</h3><p>Does your product refuse to scale? Is it bogged down by unpredictable,</p></div>
    <div class="offer-item"><svg viewBox="0 0 40 40"><rect x="6" y="22" width="8" height="12"/><rect x="16" y="14" width="8" height="20"/><rect x="26" y="8" width="8" height="26"/></svg><h3>Agile Consulting</h3><p>Steady delivery practice along the highway will close the loop on focusing solely on the bottom line.</p></div>
    <div class="offer-item"><svg viewBox="0 0 40 40"><path d="M6 34h28M10 34V24l10-8 4 4 8-12"/></svg><h3>SMEs</h3><p>Keeping your eye on the ball while performing a deep dive on the startup product mentality.</p></div>
    <div class="offer-item"><svg viewBox="0 0 40 40"><path d="M8 34V14l12-8 12 8v20z"/><path d="M16 34V22h8v12"/></svg><h3>High end Training</h3><p>Strengthen lasting team relationships via premier markets. Dynamically renew resource-leveling service.</p></div>
    <div class="offer-item"><svg viewBox="0 0 40 40"><path d="M6 34V18l8 6V14l8 6V8h12v26z"/></svg><h3>Custom Development</h3><p>Seamlessly empower fully researched growth strategies and interoperable internal or "organic" sources.</p></div>
    <div class="offer-item"><svg viewBox="0 0 40 40"><path d="M20 4c6 8 10 13 10 20a10 10 0 0 1-20 0c0-7 4-12 10-20z"/><circle cx="20" cy="24" r="4"/></svg><h3>Predictive Analytics</h3><p>Seamlessly empower fully researched growth strategies and interoperable internal or "organic" sources.</p></div>
  </div>
</section>

<section class="testimonials">
  <div class="eyebrow">What our clients say</div>
  <h2 class="heading">Testimonials about our<br>service</h2>
  <span class="underline" style="margin-top:10px"></span>
  <div class="quote-grid">
    <div class="portrait" role="img" aria-label="Black and white portrait of a bearded client"></div>
    <div class="quote">"Perfection is achieved not when there is nothing more to add, but when there is nothing left to take away."<cite>Marcel Dufrene</cite></div>
    <div class="portrait" role="img" aria-label="Black and white portrait of a smiling client"></div>
    <div class="quote">"We are what we repeatedly do. Excellence, then, is not an act, but a habit."<cite>Theron of Kos</cite></div>
    <div class="quote">"Look deep into nature, and you will understand everything better."<cite>Halvard Lenz</cite></div>
    <div class="portrait" role="img" aria-label="Black and white portrait of a young client"></div>
    <div class="quote">"Lorenzo Vessari, The Notebooks, Vol. II: Anatomy, Zoology and Physiology"<cite>Ann Sorel</cite></div>
    <div class="portrait" role="img" aria-label="Black and white portrait of a cheerful client"></div>
  </div>
</section>

<section class="background">
  <h2 class="heading">Background &amp; Expertise</h2>
  <span class="underline"></span>
  <div class="copy">
    <p>We are primarily server side programmers with expertise in large scale projects – be it Software development tools, Distributed software frameworks, Telecom and mediation software or Business intelligence.</p>
    <p>Over the years, we have been the trusted offshore product development partner for many startups and mid sized software product companies, and have built software products from scratch.</p>
    <p>We have built over 10 software products for startups all over the world. Best in class UI, and APIs have been designed and implemented by us. Often we take a core technology developed in a university, or an idea, and build a product around it.</p>
    <p>We work in cloud, mobile apps, big data and analytics. We are now getting into predictive analytics, machine learning and AI.</p>
    <p>We have been associated with the leaders of the Agile movement, and have expertise implementing agile practices in Brivolt Software as well as other companies.</p>
    <p>We have expertise in Design and architectural interventions – taking a flawed product and breathing life back into it.</p>
    <p>We conduct high-end training in Scrum, clean code, and clean design inspired by Coach Bert. We conduct training in Java, and concurrency.</p>
  </div>
</section>

<section class="clients">
  <h2 class="heading">Our Clients</h2>
  <span class="underline"></span>
  <div class="client-row">
    <div class="client"><i></i>Calmora</div>
    <div class="client"><i></i>Ledgerly</div>
    <div class="client"><i></i>Wexmoor</div>
    <div class="client"><i></i>Hartline</div>
    <div class="client"><i></i>Tempo Ridge</div>
    <div class="client"><i></i>Veltro</div>
  </div>
</section>

<footer class="footer">
  <div class="footer-texture"></div>
  <div class="footer-col" style="left:142px">
    <div class="label">Marlow Bay</div>
    <h4>Headquarters</h4>
    <p>Interactively coordinate proactive "outside the box" thinking.</p>
    <ul class="contact-list">
      <li><svg viewBox="0 0 12 12"><path d="M2 1l3 1 0 3-1.5 1a7 7 0 0 0 3 3l1-1.5 3 0 1 3c-6 1-11-4-9.5-9.5z"/></svg>+1 555 0190 221</li>
      <li><svg viewBox="0 0 12 12"><circle cx="6" cy="6" r="5"/></svg>www.forgeline-example.com</li>
      <li><svg viewBox="0 0 12 12"><rect x="1" y="2.5" width="10" height="7"/></svg>info@forgeline-example.com</li>
    </ul>
  </div>
  <div class="footer-col" style="left:379px">
    <div class="label">Locations</div>
    <h4>We Are Everywhere</h4>
  </div>
  <div class="world-map" role="img" aria-label="Dotted world map marking office locations"></div>
  <div class="network">
    <div class="label">OUR NETWORK</div>
    <ul>
      <li><svg viewBox="0 0 10 12"><path d="M5 0a4 4 0 0 1 4 4c0 3-4 8-4 8S1 7 1 4a4 4 0 0 1 4-4z"/></svg>Northgate + 1 555 0136 402</li>
      <li><svg viewBox="0 0 10 12"><path d="M5 0a4 4 0 0 1 4 4c0 3-4 8-4 8S1 7 1 4a4 4 0 0 1 4-4z"/></svg>Canalside + 1 555 0177 319</li>
      <li><svg viewBox="0 0 10 12"><path d="M5 0a4 4 0 0 1 4 4c0 3-4 8-4 8S1 7 1 4a4 4 0 0 1 4-4z"/></svg>Eastbrook + 1 555 0158 960</li>
    </ul>
  </div>
  <div class="footer-col" style="left:846px">
    <div class="label">Get in touch</div>
    <h4>Follow Our Activity</h4>
    <p>Interactively coordinate proactive e-commerce via process-centric "outside the box" thinking.</p>
    <div class="social"><span></span><span></span><span></span><span></span></div>
  </div>
</footer>

</body>
</html>
```